Fern Lantern Cannabis Cartridge box

Box with both inside and outside box. A disposable cannabis vape cart is the contents of the package. initial thoughts were black exterior box with color highlight. (example of 7 mint attached). There are four colors currently being used for the actual product. Black, White, Green and Blue. product will sit in retail display box. It should both "pop" and still emote quality and class.

Target Market(s)

Professional, discreet cannabis consumer. Experienced and knowledgeable

Industry/Entity Type

Cannabis

Font styles to use
Serif

Colors

Designer to choose colors to be used in the design.

Requirements
Must have
• use logo and logo colors
Nice to have
• elegant look. metalic foil printing, embossing available

```html
<!DOCTYPE html>
<html lang="en">
<head>
<meta charset="utf-8">
<title>Fern Lantern Vape Cartridge Box Range</title>
<link rel="stylesheet" href="https://fonts.googleapis.com/css2?family=Barlow:wght@500;600;700&family=Roboto:wght@500;700&display=swap">
<style>
  :root {
    --canvas-bg: #f4f5f6;
    --box-black: #1f1f20;
    --box-black-deep: #141415;
    --ink-white: #ffffff;
    --ink-dark: #2a2a2a;
    --brand-teal: #1a9e8a;
    --green-a: #17a07d;
    --green-b: #2bb597;
    --blue-a: #0a86dc;
    --blue-b: #27a4f2;
    --silver-a: #bfc0c2;
    --silver-b: #f2f2f2;
    --black-a: #232324;
    --black-b: #2e2e2f;
  }
  html, body {
    margin: 0;
    padding: 0;
    width: 1200px;
    height: 900px;
    overflow: hidden;
    background: var(--canvas-bg);
  }
  .range {
    position: relative;
    width: 1200px;
    height: 900px;
    display: flex;
    justify-content: center;
    align-items: center;
    gap: 46px;
  }
  .box {
    display: grid;
    grid-template-columns: 170px 58px;
    grid-template-rows: 58px 560px;
    filter: drop-shadow(0 18px 20px rgba(0,0,0,0.12));
  }
  .box--green  { --accent-a: var(--green-a);  --accent-b: var(--green-b);  --accent-ink: var(--ink-white); }
  .box--blue   { --accent-a: var(--blue-a);   --accent-b: var(--blue-b);   --accent-ink: var(--ink-white); }
  .box--silver { --accent-a: var(--silver-a); --accent-b: var(--silver-b); --accent-ink: var(--ink-dark); }
  .box--black  { --accent-a: var(--black-a);  --accent-b: var(--black-b);  --accent-ink: var(--ink-white); }

  .top {
    grid-column: 1;
    grid-row: 1;
    display: flex;
    align-items: center;
    justify-content: center;
    gap: 6px;
    background: linear-gradient(135deg, var(--accent-a), var(--accent-b));
    border-bottom: 1px solid rgba(0,0,0,0.18);
    font-family: "Barlow", sans-serif;
    font-weight: 700;
    font-size: 11px;
    letter-spacing: 2px;
    color: var(--accent-ink);
  }
  .top .top-dot {
    width: 8px;
    height: 8px;
    border-radius: 50%;
    background: currentColor;
  }

  .front {
    grid-column: 1;
    grid-row: 2;
    position: relative;
    width: 170px;
    height: 560px;
    background: var(--box-black);
    overflow: hidden;
  }
  .front-shapes {
    position: absolute;
    inset: 0;
    width: 170px;
    height: 560px;
  }
  .accent-stop-a { stop-color: var(--accent-a); }
  .accent-stop-b { stop-color: var(--accent-b); }
  .product-title {
    position: absolute;
    top: 78px;
    left: 0;
    width: 170px;
    text-align: center;
    font-family: "Barlow", sans-serif;
    font-weight: 600;
    font-size: 17px;
    line-height: 1.05;
    letter-spacing: 3px;
    color: var(--accent-ink);
    transform: rotate(-4deg);
  }
  .box--silver .product-title,
  .box--black .product-title { transform: rotate(4deg); }
  .brand-name {
    position: absolute;
    top: 250px;
    left: 0;
    width: 170px;
    text-align: center;
    font-family: "Barlow", sans-serif;
    font-weight: 700;
    font-size: 30px;
    line-height: 1;
    letter-spacing: 2px;
    color: var(--brand-teal);
  }
  .brand-name .brand-dot {
    display: block;
    width: 14px;
    height: 14px;
    margin: 0 auto 12px;
    border-radius: 50%;
    background: var(--brand-teal);
  }
  .product-class {
    position: absolute;
    bottom: 46px;
    left: 0;
    width: 170px;
    text-align: center;
    font-family: "Barlow", sans-serif;
    font-weight: 600;
    font-size: 8px;
    line-height: 1.3;
    letter-spacing: 2.5px;
    color: var(--accent-ink);
    transform: rotate(8deg);
  }
  .box--black .product-class { color: var(--ink-white); }
  .product-class .class-mark {
    display: block;
    width: 12px;
    height: 12px;
    margin: 0 auto 8px;
    border-radius: 50%;
    background: currentColor;
  }

  .side {
    grid-column: 2;
    grid-row: 2;
    position: relative;
    width: 58px;
    height: 560px;
    background: linear-gradient(90deg, var(--box-black-deep), var(--box-black));
    display: flex;
    flex-direction: column;
    align-items: center;
    justify-content: flex-end;
    padding-bottom: 40px;
    box-sizing: border-box;
  }
  .side-copy {
    writing-mode: vertical-rl;
    transform: rotate(180deg);
    font-family: "Roboto", sans-serif;
    font-weight: 700;
    font-size: 15px;
    color: var(--ink-white);
    white-space: nowrap;
  }
  .social-tag {
    display: flex;
    flex-direction: column;
    align-items: center;
    gap: 8px;
    margin-bottom: 16px;
  }
  .social-handle {
    writing-mode: vertical-rl;
    transform: rotate(180deg);
    font-family: "Roboto", sans-serif;
    font-weight: 500;
    font-size: 11px;
    padding: 10px 4px;
    border-radius: 4px;
    background: linear-gradient(180deg, var(--accent-b), var(--accent-a));
    color: var(--accent-ink);
    white-space: nowrap;
  }
  .box--black .social-handle { background: #2f2f30; color: var(--ink-white); }
  .social-mark {
    width: 10px;
    height: 10px;
    border-radius: 2px;
    background: var(--ink-white);
  }
</style>
</head>
<body>
<main class="range">

  <section class="box box--green">
    <div class="top"><span class="top-dot"></span>FERN LANTERN</div>
    <div class="front">
      <svg class="front-shapes" viewBox="0 0 170 560" aria-hidden="true">
        <defs>
          <linearGradient id="accent-green" x1="0" y1="0" x2="1" y2="1">
            <stop offset="0" class="accent-stop-a"/><stop offset="1" class="accent-stop-b"/>
          </linearGradient>
        </defs>
        <polygon points="0,170 85,210 170,160 170,300 0,360" fill="#262627"/>
        <polygon points="0,0 170,0 170,160 85,210 0,170" fill="url(#accent-green)"/>
        <polygon points="0,470 105,430 170,455 170,560 0,560" fill="url(#accent-green)"/>
      </svg>
      <div class="product-title">VAPE<br>CARTRIDGE</div>
      <div class="brand-name"><span class="brand-dot"></span>FERN<br>LANTERN</div>
      <div class="product-class"><span class="class-mark"></span>MARIJUANA<br>PRODUCT</div>
    </div>
    <div class="side">
      <div class="social-tag"><span class="social-handle">@FERN_LANTERN</span><span class="social-mark"></span></div>
      <div class="side-copy">We are Social. Follow Us</div>
    </div>
  </section>

  <section class="box box--blue">
    <div class="top"><span class="top-dot"></span>FERN LANTERN</div>
    <div class="front">
      <svg class="front-shapes" viewBox="0 0 170 560" aria-hidden="true">
        <defs>
          <linearGradient id="accent-blue" x1="0" y1="0" x2="1" y2="1">
            <stop offset="0" class="accent-stop-a"/><stop offset="1" class="accent-stop-b"/>
          </linearGradient>
        </defs>
        <polygon points="0,170 85,210 170,160 170,300 0,360" fill="#262627"/>
        <polygon points="0,0 170,0 170,160 85,210 0,170" fill="url(#accent-blue)"/>
        <polygon points="0,470 105,430 170,455 170,560 0,560" fill="url(#accent-blue)"/>
      </svg>
      <div class="product-title">VAPE<br>CARTRIDGE</div>
      <div class="brand-name"><span class="brand-dot"></span>FERN<br>LANTERN</div>
      <div class="product-class"><span class="class-mark"></span>MARIJUANA<br>PRODUCT</div>
    </div>
    <div class="side">
      <div class="social-tag"><span class="social-handle">@FERN_LANTERN</span><span class="social-mark"></span></div>
      <div class="side-copy">We are Social. Follow Us</div>
    </div>
  </section>

  <section class="box box--silver">
    <div class="top"><span class="top-dot"></span>FERN LANTERN</div>
    <div class="front">
      <svg class="front-shapes" viewBox="0 0 170 560" aria-hidden="true">
        <defs>
          <linearGradient id="accent-silver" x1="0" y1="0" x2="1" y2="1">
            <stop offset="0" class="accent-stop-a"/><stop offset="1" class="accent-stop-b"/>
          </linearGradient>
        </defs>
        <polygon points="0,170 85,210 170,160 170,300 0,360" fill="#262627"/>
        <polygon points="0,0 170,0 170,160 85,210 0,170" fill="url(#accent-silver)"/>
        <polygon points="0,470 105,430 170,455 170,560 0,560" fill="url(#accent-silver)"/>
      </svg>
      <div class="product-title">VAPE<br>CARTRIDGE</div>
      <div class="brand-name"><span class="brand-dot"></span>FERN<br>LANTERN</div>
      <div class="product-class"><span class="class-mark"></span>MARIJUANA<br>PRODUCT</div>
    </div>
    <div class="side">
      <div class="social-tag"><span class="social-handle">@FERN_LANTERN</span><span class="social-mark"></span></div>
      <div class="side-copy">We are Social. Follow Us</div>
    </div>
  </section>

  <section class="box box--black">
    <div class="top"><span class="top-dot"></span>FERN LANTERN</div>
    <div class="front">
      <svg class="front-shapes" viewBox="0 0 170 560" aria-hidden="true">
        <defs>
          <linearGradient id="accent-black" x1="0" y1="0" x2="1" y2="1">
            <stop offset="0" class="accent-stop-a"/><stop offset="1" class="accent-stop-b"/>
          </linearGradient>
        </defs>
        <polygon points="0,170 85,210 170,160 170,300 0,360" fill="#1a1a1b"/>
        <polygon points="0,0 170,0 170,160 85,210 0,170" fill="url(#accent-black)"/>
        <polygon points="0,470 105,430 170,455 170,560 0,560" fill="#191919"/>
      </svg>
      <div class="product-title">VAPE<br>CARTRIDGE</div>
      <div class="brand-name"><span class="brand-dot"></span>FERN<br>LANTERN</div>
      <div class="product-class"><span class="class-mark"></span>MARIJUANA<br>PRODUCT</div>
    </div>
    <div class="side">
      <div class="social-tag"><span class="social-handle">@FERN_LANTERN</span><span class="social-mark"></span></div>
      <div class="side-copy">We are Social. Follow Us</div>
    </div>
  </section>

</main>
</body>
</html>
```